Brand new leaflet design creative ideas.

I need a flyer designed for my business

I run a pay weekly carpet business and need designs for a flyer this design i will also want to enable it on letterheads business cards and a logo from it when created.

my domain name is www.pebblemarsh.co.uk / www.pebblemarsh.com

Our main competitor i have attached his design to this brief to give you a bit of an idea on how we work, however i do not want a copycat design i want a brand new design something not like theres but eye catching direct to the point.

We are open to colour suggestions as long as the colours work.
Thank you.

Target Market(s)

This print material will be delivered to customers houses.

Industry/Entity Type

Flooring

Font styles to use
Serif
Sans Serif

Requirements
Must have
• Website domain name,
• Various print options CMYK, PDF
Nice to have
• Creativity eye catching
Should not have
• SHOULD NOT BE A COPYCAT DESIGN SOMETHING NEW & CREATIVE

```html
<!DOCTYPE html>
<html lang="en">
<head>
<meta charset="utf-8">
<title>Tuftline Carpets – Leaflet</title>
<link href="https://fonts.googleapis.com/css2?family=Anton&family=Archivo+Black&family=Lato:wght@400;700&family=Oswald:wght@500;600&display=swap" rel="stylesheet">
<style>
  :root{
    --red:#d63239;
    --yellow:#ecc74a;
    --ink:#111111;
    --grey:#dcdcdc;
    --white:#ffffff;
    --page:#ffffff;
  }
  html,body{margin:0;padding:0;width:1200px;height:1200px;overflow:hidden;background:var(--page);}
  .leaflet{position:absolute;left:205px;top:71px;width:770px;height:1079px;background:var(--white);overflow:hidden;}
  .shapes{position:absolute;left:0;top:0;width:770px;height:1079px;}
  .hero-photo{position:absolute;left:0;top:0;width:770px;height:407px;
    background:linear-gradient(100deg,#efe7da 0%,#e6dccb 35%,#cfc3b8 55%,#b9aea6 75%,#e3e1de 100%);}
  .t{position:absolute;margin:0;line-height:1;white-space:nowrap;}
  .brand{position:absolute;left:0;width:400px;top:51px;text-align:center;}
  .brand-mark{display:block;width:63px;height:63px;background:var(--red);border-radius:6px;margin:0 auto 14px;}
  .brand-name{display:block;font-family:"Archivo Black",sans-serif;font-size:17px;line-height:1;letter-spacing:1px;color:var(--ink);}
  .welcome{left:26px;top:372px;font-family:"Archivo Black",sans-serif;font-size:50px;color:var(--white);}
  .welcome-brand{left:26px;top:428px;font-family:"Oswald",sans-serif;font-weight:600;font-size:36px;color:var(--yellow);}
  .about-title{right:40px;top:466px;font-family:"Archivo Black",sans-serif;font-size:24px;color:var(--red);}
  .about-body{position:absolute;right:40px;top:506px;margin:0;text-align:right;white-space:nowrap;
    font-family:"Lato",sans-serif;font-size:12.2px;line-height:15.2px;color:var(--ink);}
  .offer-text{position:absolute;left:24px;width:256px;text-align:center;margin:0;line-height:1;white-space:nowrap;}
  .offer-kicker{top:671px;font-family:"Oswald",sans-serif;font-weight:500;font-size:20px;color:var(--red);}
  .offer-label{top:696px;font-family:"Anton",sans-serif;font-size:24px;color:var(--white);}
  .offer-lead{top:714px;font-family:"Oswald",sans-serif;font-weight:600;font-size:38px;color:var(--yellow);}
  .offer-price{top:752px;font-family:"Anton",sans-serif;font-size:62px;color:var(--white);}
  .offer-unit{top:815px;font-family:"Oswald",sans-serif;font-weight:500;font-size:32px;color:var(--red);}
  .perk{position:absolute;display:flex;align-items:center;gap:6px;font-family:"Oswald",sans-serif;font-weight:500;font-size:18px;color:var(--ink);}
  .perk svg{width:18px;height:18px;}
  .terms{position:absolute;left:0;width:310px;text-align:center;margin:0;line-height:1;white-space:nowrap;}
  .terms-free{top:900px;font-family:"Anton",sans-serif;font-size:36px;color:var(--ink);}
  .terms-checks{top:945px;font-family:"Anton",sans-serif;font-size:32px;color:var(--red);}
  .terms-delay{top:981px;font-family:"Archivo Black",sans-serif;font-size:27px;color:var(--ink);}
  .terms-apply{top:1015px;font-family:"Anton",sans-serif;font-size:46px;color:var(--red);}
  .review{position:absolute;left:336px;top:871px;width:362px;margin:0;text-align:right;
    font-family:"Lato",sans-serif;font-size:12.4px;line-height:15.5px;color:var(--ink);}
  .review-quote{position:absolute;font-family:"Archivo Black",sans-serif;font-size:34px;color:var(--red);line-height:1;}
  .review-name{right:45px;top:919px;font-family:"Oswald",sans-serif;font-weight:500;font-size:13px;color:var(--red);}
  .cta-label{right:45px;top:950px;font-family:"Anton",sans-serif;font-size:32px;color:var(--red);}
  .cta-phone{right:45px;top:989px;font-family:"Anton",sans-serif;font-size:34px;color:var(--ink);}
  .cta-web{right:45px;top:1026px;font-family:"Lato",sans-serif;font-size:11px;letter-spacing:5.6px;color:var(--ink);}
</style>
</head>
<body>
<main class="leaflet">
  <div class="hero-photo" role="img" aria-label="Photo of a smiling woman in a red striped top lying on a soft grey deep-pile carpet in a bright living room"></div>

  <svg class="shapes" viewBox="0 0 770 1079" aria-hidden="true">
    <polygon points="0,225 466,413 0,633" fill="var(--red)"/>
    <rect x="0" y="668" width="770" height="162" fill="var(--yellow)"/>
    <polygon points="0,830 259,830 370,1079 0,1079" fill="var(--grey)"/>
    <polygon points="356,1048 770,1048 770,1079 370,1079" fill="var(--ink)"/>
    <circle cx="151" cy="753" r="128" fill="var(--ink)" stroke="var(--yellow)" stroke-width="5"/>
  </svg>

  <div class="brand">
    <span class="brand-mark"></span>
    <span class="brand-name">TUFTLINE CARPETS</span>
  </div>

  <h1 class="t welcome">Welcome to</h1>
  <h2 class="t welcome-brand">TUFTLINE CARPETS</h2>

  <h3 class="t about-title">About us</h3>
  <p class="about-body">We are a small family owned and run business that pride our-<br>selves on offering our customers a genuine high quality<br>product and service.<br>When you order from us you’ll be able to choose from our range of Deep Pile Bel-<br>gium carpets that will then be installed on top of premium quality British made Woolmere<br>underlay which comes with a lifetime guarantee.<br>Our fully trained fitters will then install your chosen carpet using gripper rods and door trims in the<br>traditional manner.</p>

  <p class="offer-text offer-kicker">Amazing Carpet</p>
  <p class="offer-text offer-label">OFFERS</p>
  <p class="offer-text offer-lead">Pay only</p>
  <p class="offer-text offer-price">£10.00</p>
  <p class="offer-text offer-unit">per week</p>

  <div class="perk" style="left:306px;top:720px;">
    <svg viewBox="0 0 18 18"><path d="M2 9 L9 2 L16 9 M4 7.5 V16 H14 V7.5" fill="none" stroke="var(--red)" stroke-width="1.5"/></svg>Free Home Measuring</div>
  <div class="perk" style="left:306px;top:753px;">
    <svg viewBox="0 0 18 18"><rect x="3" y="8" width="12" height="9" rx="1" fill="var(--red)"/><path d="M5.5 8 V5.5 a3.5 3.5 0 0 1 7 0 V8" fill="none" stroke="var(--red)" stroke-width="1.8"/></svg>Free Underlay</div>
  <div class="perk" style="left:552px;top:718px;">
    <svg viewBox="0 0 18 18"><rect x="2" y="6" width="14" height="4" fill="var(--red)"/><rect x="3" y="10" width="12" height="7" fill="var(--red)"/><rect x="8" y="6" width="2" height="11" fill="var(--yellow)"/></svg>Free Grippers</div>
  <div class="perk" style="left:552px;top:750px;">
    <svg viewBox="0 0 18 18"><path d="M4 17 V1.5 H14 V17 M4 2 L10 4 V17" fill="none" stroke="var(--red)" stroke-width="1.2"/></svg>Free Door Trims</div>

  <p class="terms terms-free">INTEREST FREE</p>
  <p class="terms terms-checks">NO CREDIT CHECKS</p>
  <p class="terms terms-delay">DON’T DELAY!</p>
  <p class="terms terms-apply">APPLY NOW!</p>

  <span class="review-quote" style="left:303px;top:866px;">“</span>
  <p class="review">5 Star! Great service the lads did a great job. Lovely carpet and made me happy as it feels more homely too thanks guys</p>
  <span class="review-quote" style="left:702px;top:882px;">”</span>
  <p class="t review-name">Janet Holloway, Chorley</p>

  <p class="t cta-label">CALL FREE NOW ON:</p>
  <p class="t cta-phone">0800 555 0142</p>
  <p class="t cta-web">www.pebblemarsh.com</p>
</main>
</body>
</html>
```